eMail HTML Marketing Template

I need an HTML e-mail marketing template design based off our current website theme (www.trelvane.com). If you need anymore info or have questions please let me know and I will get back to you ASAP.

Goal: A monthly newsletter template for email marketing. Please use lorem ipsum for content filler. If you need to purchase images for the design please let me know and the price to do so.

Thanks.

***URGENT***
If anyone can provide a well designed mockup by 4:00PM EST today (2/6/13) I will award up to two participation prizes of $20 each to each submitter.

Goal: A monthly newsletter template for email marketing.  Please use lorem ipsum for content filler. If you need to purchase images for the design please let me know and the price to do so.

Thanks.

***URGENT***

```html
<!DOCTYPE html>
<html lang="en">
<head>
<meta charset="utf-8">
<title>Trelvane Monthly Newsletter</title>
<link rel="stylesheet" href="https://fonts.googleapis.com/css2?family=Open+Sans:wght@300;400;600;700&family=Ubuntu:wght@400;500;700&display=swap">
<style>
  :root {
    --green: #5aa70a;
    --black: #000000;
    --charcoal: #1f1f1f;
    --blue-top: #3a5fa8;
    --blue-bottom: #1f3d80;
    --ink: #1c1c1c;
    --rule: #d9d9d9;
    --white: #ffffff;
    --photo-street-a: #d8d2c8;
    --photo-street-b: #9c958c;
    --photo-girls-a: #f2e6d0;
    --photo-girls-b: #c9a15a;
    --photo-bags-a: #f4a6c6;
    --photo-bags-b: #44b4e0;
    --coupon-bag: #f3a81b;
  }
  * { margin: 0; padding: 0; box-sizing: border-box; }
  html, body { width: 1200px; height: 2240px; overflow: hidden; background: var(--white); }
  body { position: relative; font-family: "Ubuntu", "Trebuchet MS", sans-serif; color: var(--ink); }
  .abs { position: absolute; }

  .logo-block { left: 0; top: 0; width: 506px; height: 226px; background: var(--black); display: flex; align-items: center; padding-left: 92px; gap: 16px; }
  .logo-dot { width: 40px; height: 40px; border-radius: 50%; background: var(--green); }
  .logo-name { font-family: "Open Sans", sans-serif; font-weight: 700; font-size: 44px; color: var(--white); letter-spacing: 1px; }

  .hero-headline { left: 0; top: 226px; width: 506px; height: 334px; background: var(--green); padding: 66px 0 0 82px; font-family: "Open Sans", sans-serif; color: var(--white); font-size: 58px; line-height: 62px; font-weight: 300; white-space: nowrap; }
  .hero-headline strong { font-weight: 600; font-size: 45px; }

  .hero-photo { left: 506px; top: 0; width: 694px; height: 560px; background: linear-gradient(135deg, var(--photo-street-a), var(--photo-street-b)); }
  .issue-date { left: 1038px; top: 0; width: 162px; height: 299px; background: rgba(255,255,255,0.92); }
  .issue-date span { position: absolute; left: 50%; top: 50%; transform: translate(-50%, -50%) rotate(-90deg); white-space: nowrap; font-family: "Open Sans", sans-serif; font-size: 28px; color: var(--ink); }

  .rule { left: 82px; width: 1038px; height: 2px; background: var(--rule); }

  .intro { left: 77px; top: 592px; width: 1020px; font-family: "Open Sans", sans-serif; font-size: 24px; line-height: 36px; }

  .freebie-btn { left: 726px; top: 810px; width: 394px; height: 76px; border-radius: 14px; background: linear-gradient(var(--blue-top), var(--blue-bottom)); color: var(--white); font-family: "Open Sans", sans-serif; font-size: 25px; display: flex; align-items: center; padding-left: 130px; white-space: nowrap; }
  .coupon-bag { left: 740px; top: 758px; width: 108px; height: 118px; background: var(--coupon-bag); border-radius: 6px; transform: rotate(-6deg); z-index: 2; }

  .girls-photo { left: 0; top: 896px; width: 448px; height: 370px; background: linear-gradient(120deg, var(--photo-girls-a), var(--photo-girls-b)); }
  .feature-green { left: 362px; top: 927px; width: 758px; height: 334px; background: var(--green); color: var(--white); padding: 36px 48px 0 90px; }
  .feature-title { font-family: "Open Sans", sans-serif; font-size: 37px; font-weight: 400; margin-bottom: 18px; white-space: nowrap; }
  .feature-body { font-size: 20px; line-height: 31.5px; font-weight: 500; }

  .deal-col { top: 1310px; width: 474px; }
  .deal-btn { height: 76px; border-radius: 14px; background: linear-gradient(var(--blue-top), var(--blue-bottom)); color: var(--white); font-family: "Open Sans", sans-serif; font-size: 28px; display: flex; align-items: center; padding-left: 30px; gap: 28px; white-space: nowrap; }
  .deal-text { font-size: 20px; line-height: 31.5px; font-weight: 500; padding: 22px 30px 0 12px; }
  .col-divider { left: 600px; top: 1315px; width: 2px; height: 226px; background: var(--rule); }

  .feature-dark { left: 84px; top: 1603px; width: 759px; height: 334px; background: var(--charcoal); color: var(--white); padding: 36px 48px 0 90px; }
  .bags-photo { left: 870px; top: 1606px; width: 330px; height: 330px; background: linear-gradient(135deg, var(--photo-bags-a), var(--coupon-bag), var(--photo-bags-b)); }

  .social { left: 492px; top: 2028px; width: 216px; height: 52px; display: flex; justify-content: space-between; }
  .social span { width: 52px; height: 52px; border-radius: 50%; border: 4px solid var(--black); }

  .footer-bar { left: 0; top: 2090px; width: 1200px; height: 80px; background: var(--black); color: var(--white); text-align: center; font-family: "Open Sans", sans-serif; font-size: 22px; line-height: 28px; padding-top: 12px; }
  .footer-band { left: 0; top: 2170px; width: 1200px; height: 70px; background: var(--green); }
</style>
</head>
<body>
  <header>
    <div class="abs logo-block"><span class="logo-dot"></span><span class="logo-name">Trelvane</span></div>
    <h1 class="abs hero-headline">GRAB YOUR<br><strong>FREE CUSTOMERS</strong><br>TODAY!</h1>
    <div class="abs hero-photo" role="img" aria-label="Photo of a smiling couple carrying shopping bags on a city street"></div>
    <div class="abs issue-date"><span>FEBRUARY 2013</span></div>
  </header>

  <div class="abs rule" style="top:563px"></div>

  <p class="abs intro">This is Trelvane's gift to you as we launch our business. Using our unique social media platform, we will present your business to millions of consumers as we launch. Simply use and activate a Discount Deal or place items to our MarketPlace to take advantage of this deal. Trelvane will deliver 1...</p>

  <a class="abs freebie-btn">VIEW THIS FREEBIE!</a>
  <div class="abs coupon-bag" role="img" aria-label="Illustration of an orange shopping bag with a percent sign"></div>

  <section>
    <div class="abs girls-photo" role="img" aria-label="Photo of two young women holding shopping bags"></div>
    <div class="abs feature-green">
      <h2 class="feature-title">BETA TEST DISCOUNT DEAL</h2>
      <p class="feature-body">Lorem Ipsum has been the industry's standard dummy text ever since the 1500s, when an unknown printeley of type and scrambled it to make a type specimen book. Lorem Ipsum has been the industry's standard dummy text ever since the 1500s, when an unknown printeley of type and scrambled it to make a type specimen book.</p>
    </div>
  </section>

  <div class="abs rule" style="top:1286px"></div>

  <section>
    <div class="abs deal-col" style="left:82px">
      <div class="deal-btn"><svg width="16" height="26" viewBox="0 0 16 26"><path d="M3 3l10 10-10 10" fill="none" stroke="#fff" stroke-width="4"/></svg>DISCUNT DEALS</div>
      <p class="deal-text">Lorem Ipsum has been the industry's standard dummy text ever since the 1500s, when an unknown printeley of type and scrambled it to make a type specimen book.</p>
    </div>
    <div class="abs col-divider"></div>
    <div class="abs deal-col" style="left:647px">
      <div class="deal-btn"><svg width="16" height="26" viewBox="0 0 16 26"><path d="M3 3l10 10-10 10" fill="none" stroke="#fff" stroke-width="4"/></svg>FEATURED DEALS</div>
      <p class="deal-text">Lorem Ipsum has been the industry's standard dummy text ever since the 1500s, when an unknown printeley of type and scrambled it to make a type specimen book.</p>
    </div>
  </section>

  <div class="abs rule" style="top:1573px"></div>

  <section>
    <div class="abs feature-dark">
      <h2 class="feature-title">BETA TEST DISCOUNT DEAL</h2>
      <p class="feature-body">Lorem Ipsum has been the industry's standard dummy text ever since the 1500s, when an unknown printeley of type and scrambled it to make a type specimen book. Lorem Ipsum has been the industry's standard dummy text ever since the 1500s, when an unknown printeley of type and scrambled it to make a type specimen book.</p>
    </div>
    <div class="abs bags-photo" role="img" aria-label="Photo of colourful paper shopping bags"></div>
  </section>

  <div class="abs rule" style="top:1993px"></div>

  <footer>
    <div class="abs social" aria-label="Social links"><span></span><span></span><span></span></div>
    <div class="abs footer-bar">You are receiving this email as a part of your company's program.<br>Copyright © 2012 Trelvane All rights reserved.</div>
    <div class="abs footer-band"></div>
  </footer>
</body>
</html>
```